Gourmet cookie company needs a label designed

We need a label designed for a new cookie company. We make mini cookies. The labels will be placed on either white tins or clear containers. We would like some bright and eye catching label although not child like. Our target customer is adults not kids.
Any color/colors acceptable. The initial label will be a square 4" label but the design should also be able to be formatted to fit on a round label as well in the future.

Text on label: Rosalind's Wafer Crumb Company; Chocolate Chip; All Natural; New Wt. 8.0oz

```html
<!DOCTYPE html>
<html lang="en">
<head>
<meta charset="utf-8">
<title>Rosalind's Wafer Crumb Company – Chocolate Chip Label</title>
<link rel="stylesheet" href="https://fonts.googleapis.com/css2?family=Cherry+Swash:wght@700&family=Josefin+Sans:wght@600&display=swap">
<style>
  :root {
    --cocoa: #52301c;
    --peach: #fbc9b0;
    --cherry-top: #ea2e25;
    --cherry-bottom: #8c2a1e;
    --ink: #34150f;
    --teal: #1f4e5f;
    --white: #ffffff;
  }
  html, body {
    margin: 0;
    padding: 0;
    width: 1200px;
    height: 1200px;
    overflow: hidden;
    background: var(--peach);
  }
  .label {
    display: block;
    width: 1200px;
    height: 1200px;
  }
  .stripe-light { fill: var(--peach); }
  .stripe-dark { fill: var(--cocoa); }
  .pattern-field { fill: var(--teal); }
  .cookie-frame { fill: var(--white); }
  .title-backing { fill: var(--white); }
  .brand-name,
  .brand-line {
    font-family: "Cherry Swash", Georgia, serif;
    font-weight: 700;
    fill: var(--ink);
  }
  .brand-name { font-size: 160px; }
  .brand-line { font-size: 52px; }
  .flavor {
    font-family: "Cherry Swash", Georgia, serif;
    font-weight: 700;
    font-size: 34px;
    fill: var(--white);
  }
  .claim {
    font-family: "Josefin Sans", Arial, sans-serif;
    font-weight: 600;
    font-size: 22px;
    letter-spacing: 7px;
    fill: var(--white);
  }
  .net-weight {
    font-family: "Josefin Sans", Arial, sans-serif;
    font-weight: 600;
    font-size: 26px;
    font-variant: small-caps;
    fill: var(--white);
  }
</style>
</head>
<body>
<svg class="label" viewBox="0 0 1200 1200" xmlns="http://www.w3.org/2000/svg">
  <defs>
    <linearGradient id="cookie-fill" x1="0" y1="0" x2="0" y2="1">
      <stop offset="0" stop-color="var(--cherry-top)"/>
      <stop offset="1" stop-color="var(--cherry-bottom)"/>
    </linearGradient>
  </defs>

  <g class="awning-stripes">
    <rect class="stripe-light" x="0" y="0" width="1200" height="1200"/>
    <rect class="stripe-dark" x="75" y="0" width="150" height="1200"/>
    <rect class="stripe-dark" x="375" y="0" width="150" height="1200"/>
    <rect class="stripe-dark" x="675" y="0" width="150" height="1200"/>
    <rect class="stripe-dark" x="975" y="0" width="150" height="1200"/>
  </g>

  <path class="pattern-field" role="img" aria-label="Blue polka dot pattern"
        d="M0 900 Q600 660 1200 900 L1200 1200 L0 1200 Z"/>

  <g class="cookie" role="img" aria-label="Red bitten cookie with chocolate chips">
    <circle class="cookie-frame" cx="600" cy="595" r="366"/>
    <circle cx="600" cy="595" r="350" fill="url(#cookie-fill)"/>
  </g>

  <g class="title-backing">
    <rect x="118" y="588" width="964" height="168" rx="72"/>
    <rect x="282" y="742" width="636" height="88" rx="44"/>
  </g>

  <g class="brand">
    <text class="brand-name" x="600" y="722" text-anchor="middle" textLength="880" lengthAdjust="spacingAndGlyphs">Rosalind's</text>
    <text class="brand-line" x="600" y="803" text-anchor="middle" textLength="570" lengthAdjust="spacingAndGlyphs">Wafer Crumb Company</text>
  </g>

  <text class="flavor" x="600" y="862" text-anchor="middle">Chocolate Chip</text>
  <text class="claim" x="603" y="893" text-anchor="middle">ALL NATURAL</text>

  <text class="net-weight" x="600" y="1168" text-anchor="middle">New Wt. 8.0oz</text>
</svg>
</body>
</html>
```